wedding DJ & Lighting entertainment

We are a DJ and Lighting production company. We specialize mainly in wedding entertainment. I've attached my old postcard in the image folder, however, i would like something new and updated. You can use the same bullet points from the front page, but i would like to have a cleaner look on the front. I'd like to have one large image on the front side and smaller images on the back side. I'd also like to have some text below the logo. I'd like it to say DJ * Lighting * Audio/Visual. I'd also like to have the phrase "Celebrate with Style"

Target Market(s)

weddings, private events, women

Industry/Entity Type

It Company

Font styles to use
Sans Serif
Script

Requirements
Must have
• look elegant, sophisticated. Must have my new logo! My logo is attached as one of the files. It's a headphone logo.

```html
<!DOCTYPE html>
<html lang="en">
<head>
<meta charset="utf-8">
<title>Crescendo Events – Wedding DJ &amp; Lighting Postcard</title>
<link rel="stylesheet" href="https://fonts.googleapis.com/css2?family=Lato:ital,wght@0,400;0,700;0,900;1,400;1,700&family=Great+Vibes&family=Parisienne&display=swap">
<style>
  :root {
    --purple: #4b2a73;
    --purple-deep: #3a1d5c;
    --gold: #c49a3a;
    --gold-light: #e2c27a;
    --ink: #333138;
    --paper: #ffffff;
    --paper-grey: #e9e9ec;
    --backdrop: #d8d4cc;
  }
  * { margin: 0; padding: 0; box-sizing: border-box; }
  html, body { width: 900px; height: 1200px; overflow: hidden; }
  body {
    background: var(--backdrop);
    font-family: "Lato", Arial, sans-serif;
    position: relative;
  }
  .card {
    position: absolute;
    left: 123px;
    width: 656px;
    height: 510px;
    background: var(--paper);
    overflow: hidden;
    box-shadow: 0 4px 14px rgba(0,0,0,.18);
  }
  .card--front { top: 63px; background: linear-gradient(100deg, #ffffff 0%, #f3f3f5 40%, var(--paper-grey) 75%); }
  .card--back { top: 622px; height: 513px; }
  .card__art { position: absolute; inset: 0; width: 100%; height: 100%; }

  /* brand */
  .brand {
    position: absolute;
    display: flex; align-items: center; gap: 6px;
    color: var(--purple);
    font-weight: 700;
  }
  .brand__dot { border-radius: 50%; background: var(--purple); }
  .card--front .brand { left: 48px; top: 52px; font-size: 24px; }
  .card--front .brand__dot { width: 14px; height: 14px; }
  .card--back .brand { left: 103px; top: 160px; font-size: 15px; }
  .card--back .brand__dot { width: 9px; height: 9px; }

  .services-line {
    position: absolute; left: 204px; top: 24px;
    font-weight: 900; font-size: 23px; line-height: 27px; color: var(--purple);
  }
  .services-line span { display: block; color: var(--ink); font-size: 20px; padding-left: 0; }

  .tagline {
    position: absolute; left: 24px; top: 94px;
    font-family: "Great Vibes", cursive;
    font-size: 40px; color: var(--gold);
    white-space: nowrap;
  }
  .tagline em { font-style: normal; color: var(--purple); }

  .services-label {
    position: absolute; left: 0; top: 145px;
    width: 202px; height: 31px;
    background: linear-gradient(90deg, var(--gold), var(--gold-light));
    border-radius: 0 16px 16px 0;
    color: var(--purple-deep);
    font-weight: 700; font-style: italic; font-size: 18px;
    padding: 4px 0 0 28px;
  }
  .services-list {
    position: absolute; left: 30px; top: 194px;
    list-style: none;
    font-style: italic; font-size: 17.5px; line-height: 26px; color: #4a4850;
  }
  .services-list li::before {
    content: ""; display: inline-block;
    width: 7px; height: 7px; border-radius: 50%;
    background: var(--purple); margin-right: 8px; vertical-align: 3px;
  }
  .motto {
    position: absolute; left: 34px; top: 340px;
    font-family: "Parisienne", cursive;
    font-size: 29px; line-height: 30px; color: var(--purple);
  }
  .motto span { color: var(--ink); display: block; }

  .web-band {
    position: absolute; left: 0; bottom: 0;
    width: 100%; height: 47px;
    background: var(--purple);
    color: #fff; text-align: center;
    font-size: 15px; letter-spacing: 3px; padding-top: 14px;
    padding-left: 200px;
  }

  /* back */
  .story {
    position: absolute; left: 20px; top: 200px; width: 300px;
    font-style: italic; font-size: 12.6px; line-height: 13px; color: #1c1b20;
  }
  .story p + p { margin-top: 8px; }
  .contact-band {
    position: absolute; left: 0; top: 321px;
    width: 330px; height: 52px;
    background: linear-gradient(90deg, var(--purple-deep), var(--purple));
    color: #fff; padding: 2px 0 0 24px;
    font-style: italic; font-weight: 700; font-size: 12.5px; line-height: 14px;
  }
  .contact-band .phone { font-size: 16px; line-height: 20px; }
  .contact-band svg { width: 10px; height: 10px; margin-right: 3px; vertical-align: -1px; fill: #fff; }
  .address {
    position: absolute; left: 22px; top: 380px;
    font-size: 13px; line-height: 15px; color: var(--purple);
  }
  .address svg { width: 9px; height: 12px; fill: var(--purple); vertical-align: -1px; }
  .stamp-box {
    position: absolute; left: 543px; top: 55px;
    width: 61px; height: 61px; border: 1.5px solid #111;
  }
  .address-lines {
    position: absolute; left: 362px; top: 265px; width: 242px;
  }
  .address-lines span { display: block; height: 31px; border-bottom: 1.3px solid #111; }
  .address-lines span:first-child { height: 0; }
</style>
</head>
<body>

<!-- FRONT -->
<section class="card card--front" aria-label="Postcard front">
  <svg class="card__art" viewBox="0 0 656 510" aria-hidden="false">
    <defs>
      <linearGradient id="ballroom" x1="0" y1="0" x2="0" y2="1">
        <stop offset="0" stop-color="#8a6a4a"/><stop offset=".5" stop-color="#3a2a30"/><stop offset="1" stop-color="#1c1624"/>
      </linearGradient>
      <linearGradient id="uplit" x1="0" y1="0" x2="0" y2="1">
        <stop offset="0" stop-color="#6f78c8"/><stop offset="1" stop-color="#3d3373"/>
      </linearGradient>
      <linearGradient id="dance" x1="0" y1="0" x2="1" y2="1">
        <stop offset="0" stop-color="#5a3c64"/><stop offset=".6" stop-color="#2a2230"/><stop offset="1" stop-color="#cfc7c6"/>
      </linearGradient>
      <linearGradient id="goldFront" x1="0" y1="0" x2="1" y2="1">
        <stop offset="0" stop-color="#e2c27a"/><stop offset="1" stop-color="#b3852c"/>
      </linearGradient>
    </defs>
    <!-- soft flourish tint -->
    <path d="M0 300 C60 230 140 240 220 200 L220 280 C150 300 70 330 0 380Z" fill="#dcdce0" opacity=".5"/>
    <!-- gold sweep framing photos -->
    <path d="M375 0 C445 40 402 160 395 260 C392 320 360 380 195 462 L195 462 L656 462 L656 0Z" fill="url(#goldFront)"/>
    <g role="img" aria-label="Photo: decorated wedding reception ballroom with chandelier and draped ceiling">
      <path d="M390 0 C450 40 415 160 412 262 L656 262 L656 0Z" fill="url(#ballroom)"/>
    </g>
    <g role="img" aria-label="Photo: ballroom dance floor with blue uplighting and monogram projection">
      <path d="M412 276 C470 262 560 262 656 270 L656 462 L470 462 C450 400 430 330 412 276Z" fill="url(#uplit)"/>
    </g>
    <g role="img" aria-label="Photo: bride and groom sharing their first dance">
      <path d="M212 462 C300 410 380 340 412 280 C425 330 448 400 460 462Z" fill="url(#dance)"/>
    </g>
  </svg>

  <div class="brand"><span class="brand__dot"></span>Crescendo</div>
  <div class="services-line">DJ * Lighting<span>* Audio/Visual</span></div>
  <div class="tagline">Celebrate <em>with</em> Style</div>
  <div class="services-label">Services Provided</div>
  <ul class="services-list">
    <li>DJ &amp; Emcee Entertainment</li>
    <li>Customized lighting decor</li>
    <li>Event hosting &amp; coordination</li>
    <li>Helpful Planning Tools</li>
    <li>Personalized service</li>
  </ul>
  <div class="motto">Creating<br>memories..<span>one event<br>at a time</span></div>
  <div class="web-band">www.crescendoevents.com</div>
</section>

<!-- BACK -->
<section class="card card--back" aria-label="Postcard back">
  <svg class="card__art" viewBox="0 0 656 513">
    <defs>
      <linearGradient id="goldBack" x1="0" y1="0" x2="0" y2="1">
        <stop offset="0" stop-color="#e2c27a"/><stop offset="1" stop-color="#b3852c"/>
      </linearGradient>
      <linearGradient id="party" x1="0" y1="0" x2="1" y2="1">
        <stop offset="0" stop-color="#b04a6a"/><stop offset=".5" stop-color="#6a2c3c"/><stop offset="1" stop-color="#d9b9a8"/>
      </linearGradient>
      <linearGradient id="crowd" x1="0" y1="0" x2="0" y2="1">
        <stop offset="0" stop-color="#e6e6e6"/><stop offset=".5" stop-color="#6e6e6e"/><stop offset="1" stop-color="#2a2a2a"/>
      </linearGradient>
      <linearGradient id="paneShade" x1="0" y1="0" x2="1" y2="0">
        <stop offset="0" stop-color="#ffffff"/><stop offset="1" stop-color="#e4e4e8"/>
      </linearGradient>
    </defs>
    <!-- left panel with curved edge -->
    <path d="M0 0 L300 0 C330 80 345 200 320 300 C305 360 290 420 300 513 L0 513Z" fill="url(#paneShade)"/>
    <path d="M300 0 C345 70 352 200 328 300 C313 362 300 430 310 513 L300 513 C292 420 305 360 320 300 C345 200 330 80 300 0Z" fill="url(#goldBack)"/>
    <path d="M320 0 L312 0 C355 80 350 220 336 300 L344 300 C358 210 362 90 320 0Z" fill="var(--purple)"/>
    <!-- gold curve beneath top photo -->
    <path d="M0 125 C70 150 180 140 300 95 L300 110 C180 158 70 165 0 140Z" fill="url(#goldBack)"/>
    <g role="img" aria-label="Photo: wedding guests dancing together on a lit dance floor">
      <path d="M0 0 L310 0 L300 95 C180 140 70 150 0 125Z" fill="url(#party)"/>
    </g>
    <circle cx="287" cy="83" r="78" fill="url(#goldBack)"/>
    <g role="img" aria-label="Photo: excited party crowd raising hands, black and white">
      <circle cx="287" cy="83" r="70" fill="url(#crowd)"/>
    </g>
  </svg>

  <div class="brand"><span class="brand__dot"></span>Crescendo</div>
  <div class="story">
    <p>We know planning your big day can be a little overwhelming. You have to coordinate with so many different people along the way.</p>
    <p>With years of entertainment and production experience, we make sure your occasion comes to life for you and your guests. After all, it's your day, your event and your memories ...it's about you.</p>
  </div>
  <div class="contact-band">
    <div class="phone"><svg viewBox="0 0 10 10"><path d="M2 0.5 L3.8 2.8 L2.8 3.8 C3.4 5 5 6.6 6.2 7.2 L7.2 6.2 L9.5 8 L8.3 9.5 C4.5 9.2 0.8 5.5 0.5 1.7Z"/></svg>888-555-0142</div>
    <div><svg viewBox="0 0 10 10"><circle cx="5" cy="5" r="4.5"/></svg>crescendoevents.com</div>
    <div><svg viewBox="0 0 10 10"><path d="M0 2 H10 V8.5 H0Z M0.8 2.6 L5 5.6 L9.2 2.6" /></svg>hello@crescendoevents.com</div>
  </div>
  <div class="address">
    <svg viewBox="0 0 9 12"><path d="M4.5 0 C7 0 9 2 9 4.4 C9 7.3 4.5 12 4.5 12 C4.5 12 0 7.3 0 4.4 C0 2 2 0 4.5 0Z"/></svg>2210 W. Harbor Ave.<br>&nbsp;&nbsp;Suite B Fullerton, CA 92833
  </div>

  <div class="stamp-box" aria-label="Stamp area"></div>
  <div class="address-lines" aria-label="Mailing address lines"><span></span><span></span><span></span></div>
</section>

</body>
</html>
```